The Kestrel Personal Training Studio Information Card

The front and back of card to give people that walk in to our gym. There are a few things to say on the card. But it also needs to be designed in an attractive way. You can make some of the information bullett points or with icons or graphics. Please look at our website at https://thekestrelfitness-example.com/ . The card will be 4" x 9"

Target Market(s)

High End Clientele who want to train in a private gym

Industry/Entity Type

Fitness

Font styles to use
Serif
Sans Serif
Other font styles liked:
• the same font Vorlex uses on the zuntab

Colors
F0912C
F2A743
F7CA91
FBE8D2
FDF5EE

Requirements
Must have
• A cool look

```html
<!DOCTYPE html>
<html lang="en">
<head>
<meta charset="utf-8">
<title>The Kestrel Personal Training Studio – Information Card</title>
<link rel="stylesheet" href="https://fonts.googleapis.com/css2?family=Exo+2:ital,wght@0,700;1,700;1,800;1,900&family=Roboto:wght@400;500&display=swap">
<style>
  :root {
    --orange: #ef4b24;
    --orange-deep: #c9361a;
    --ink: #121212;
    --ink-soft: #1d1d1d;
    --white: #ffffff;
    --grey: #b9bbbd;
    --stage: #dcdcdc;
    --skin: #6b3a26;
    --head: "Exo 2", "Arial Narrow", sans-serif;
    --body: "Roboto", Arial, sans-serif;
  }
  * { box-sizing: border-box; margin: 0; padding: 0; }
  html, body { width: 945px; height: 1200px; overflow: hidden; background: var(--stage); }
  .stage {
    width: 945px; height: 1200px;
    display: flex; align-items: center; justify-content: center; gap: 33px;
  }
  .card {
    position: relative; width: 270px; height: 607px; overflow: hidden;
    background: var(--ink); color: var(--white); font-family: var(--body);
    box-shadow: 0 6px 16px rgba(0,0,0,.28);
  }
  .card > * { position: absolute; }
  .shapes { inset: 0; width: 270px; height: 607px; }

  .photo {
    left: 0; top: 60px; width: 270px; height: 290px;
    background: radial-gradient(ellipse 45% 50% at 55% 45%, #8a4a2f 0%, #4a2619 45%, rgba(18,18,18,0) 80%);
  }

  .brand { left: 20px; top: 24px; }
  .brand-name {
    display: block; font-family: var(--head); font-weight: 700; font-style: normal;
    color: var(--orange); font-size: 27px; line-height: 1; letter-spacing: .5px; text-transform: uppercase;
  }
  .brand-tag {
    display: block; margin-top: 4px; font-family: var(--body); font-weight: 500;
    font-size: 6.6px; letter-spacing: 2.3px; color: var(--white);
  }

  .kicker {
    left: 32px; top: 236px; font-family: var(--head); font-style: italic; font-weight: 800;
    font-size: 19px; line-height: 26px; color: var(--white);
  }
  .headline-get {
    left: 20px; top: 262px; font-family: var(--head); font-style: italic; font-weight: 900;
    font-size: 72px; line-height: 70px; color: var(--orange); letter-spacing: -1px;
  }
  .headline-started {
    left: 20px; top: 338px; font-family: var(--head); font-style: italic; font-weight: 900;
    font-size: 45px; line-height: 46px; color: var(--orange); letter-spacing: -.5px;
  }
  .chevrons { left: 210px; top: 322px; width: 36px; height: 18px; }
  .intro { left: 20px; top: 398px; width: 235px; font-size: 12.4px; line-height: 16.8px; }

  .card--light .kicker, .card--light .headline-get, .card--light .headline-started { color: var(--white); }
  .card--light .kicker { top: 238px; }
  .card--light .intro { top: 400px; width: 210px; }

  /* back */
  .lead {
    left: 24px; top: 46px; width: 220px; font-family: var(--head); font-style: italic; font-weight: 700;
    font-size: 16.5px; line-height: 20.5px; color: var(--orange);
  }
  .copy { left: 24px; width: 222px; font-size: 9.6px; line-height: 12.9px; }
  .copy--goals { top: 120px; }
  .copy--safety { top: 199px; text-align: justify; }
  .rates-title {
    left: 26px; top: 300px; font-family: var(--head); font-style: italic; font-weight: 800;
    font-size: 26px; line-height: 30px; color: var(--orange);
  }
  .rates-note {
    left: 26px; top: 334px; font-family: var(--head); font-style: italic; font-weight: 700;
    font-size: 6.8px; color: var(--white); letter-spacing: .2px;
  }
  .rate-list { left: 24px; top: 356px; width: 222px; list-style: none; }
  .rate { display: flex; gap: 5px; height: 23px; margin-bottom: 6px; }
  .rate-freq {
    width: 116px; background: var(--white); color: var(--ink); border-radius: 3px;
    font-family: var(--head); font-style: italic; font-weight: 700; font-size: 11.5px;
    display: flex; align-items: center; padding-left: 8px;
  }
  .rate-price {
    flex: 1; background: var(--orange); border-radius: 3px; display: flex; align-items: center;
    padding-left: 8px; gap: 11px;
  }
  .rate-amount { font-family: var(--head); font-style: italic; font-weight: 800; font-size: 15px; }
  .rate-unit { font-family: var(--head); font-style: italic; font-weight: 700; font-size: 5.6px; line-height: 6px; }
  .partner {
    left: 24px; top: 452px; font-family: var(--head); font-style: italic; font-weight: 700; font-size: 11px;
  }
  .partner em { color: var(--orange); font-style: italic; }
  .partner-note { left: 24px; top: 470px; width: 215px; font-size: 7.6px; line-height: 10px; color: #d5d5d5; }
  .divider { left: 24px; top: 506px; width: 222px; height: 1px; background: var(--orange); }
  .contacts { left: 24px; top: 524px; width: 230px; display: grid; grid-template-columns: 118px 112px; row-gap: 10px; list-style: none; }
  .contact { display: flex; align-items: center; gap: 5px; font-size: 7.4px; }
  .contact svg { width: 10px; height: 10px; flex: none; }
</style>
</head>
<body>
<main class="stage">

  <!-- Front -->
  <article class="card card--dark">
    <div class="photo" role="img" aria-label="Photo of a muscular athlete, torso lit from above in a dark gym"></div>
    <svg class="shapes" viewBox="0 0 270 607" aria-hidden="true">
      <polygon points="0,172 72,110 72,156 0,212" fill="var(--orange)"/>
      <polygon points="270,28 270,38 220,94 212,94" fill="var(--grey)"/>
      <polygon points="20,236 200,236 184,263 20,263" fill="var(--orange)"/>
      <polygon points="175,330 270,246 270,260 188,330" fill="var(--white)"/>
      <polygon points="270,460 270,607 180,607" fill="var(--orange)"/>
      <polygon points="95,607 104,607 130,584 121,584" fill="var(--grey)"/>
    </svg>
    <div class="brand"><span class="brand-name">The Kestrel</span><span class="brand-tag">PRIVATE TRAINING STUDIO</span></div>
    <h2 class="kicker">HOW DO YOU</h2>
    <p class="headline-get">GET</p>
    <p class="headline-started">STARTED?</p>
    <svg class="chevrons" viewBox="0 0 36 18" aria-hidden="true"><path d="M2 2l8 7-8 7M12 2l8 7-8 7M22 2l8 7-8 7" fill="none" stroke="var(--orange)" stroke-width="3"/></svg>
    <p class="intro">We schedule prospective clients for a no cost or obligation consultation. At that consultation we will do a movement screen with you. This will allow the trainer to see what level of flexibility and strength you are currently at. You will be able to discuss your goals and other issues (injuries, etc) at that time.</p>
  </article>

  <!-- Back -->
  <article class="card card--back">
    <svg class="shapes" viewBox="0 0 270 607" aria-hidden="true">
      <polygon points="0,0 60,0 0,50" fill="var(--orange)"/>
      <polygon points="270,36 270,94 258,106 258,48" fill="var(--orange)"/>
      <polygon points="0,532 12,520 12,578 0,590" fill="var(--grey)"/>
      <polygon points="270,540 270,607 200,607" fill="var(--orange)"/>
      <polygon points="68,607 77,607 104,584 95,584" fill="var(--grey)"/>
    </svg>
    <h2 class="lead">A Safe and Individualized approach to strength training.</h2>
    <p class="copy copy--goals">Our clients have different goals: Build strength, Increase Flexibility, Improve functional and daily movements, Train for an event, or Weight Loss. We will tailor your training program to the specific results you are looking for.</p>
    <p class="copy copy--safety">Some ways of training increase the chance of injury, we do not practice those types of training at The Kestrel. Many of our clients have current or past injuries that can cause problems. We work with them to not aggravate those injuries or allow them to become an obstacle to their workouts.</p>
    <h3 class="rates-title">Our Rates:</h3>
    <p class="rates-note">ALL SESSIONS ARE 60 MINUTES</p>
    <ul class="rate-list">
      <li class="rate"><span class="rate-freq">1 Time Per Week</span><span class="rate-price"><span class="rate-amount">$110</span><span class="rate-unit">PER<br>SESSION</span></span></li>
      <li class="rate"><span class="rate-freq">2 Time Per Week</span><span class="rate-price"><span class="rate-amount">$85</span><span class="rate-unit">PER<br>SESSION</span></span></li>
      <li class="rate"><span class="rate-freq">3 Time Per Week</span><span class="rate-price"><span class="rate-amount">$80</span><span class="rate-unit">PER<br>SESSION</span></span></li>
    </ul>
    <p class="partner">Add <em>$40</em> for a Partnered Session</p>
    <p class="partner-note">Example: A Partnered Session (2 people training together) coming twice a week is $125 per session</p>
    <div class="divider"></div>
    <ul class="contacts">
      <li class="contact"><svg viewBox="0 0 10 10"><rect width="10" height="10" rx="2" fill="var(--orange)"/><path d="M5 2a2 2 0 0 0-2 2c0 1.5 2 4 2 4s2-2.5 2-4a2 2 0 0 0-2-2z" fill="#fff"/><circle cx="5" cy="4" r=".7" fill="var(--orange)"/></svg>Your Address Here</li>
      <li class="contact"><svg viewBox="0 0 10 10"><rect width="10" height="10" rx="2" fill="var(--orange)"/><path d="M3 2.3l1.2 1.5-.6.8c.4.8 1 1.4 1.8 1.8l.8-.6 1.5 1.2-.7 1C5 7.8 2.2 5 2.2 3z" fill="#fff"/></svg>000 - 000 000</li>
      <li class="contact"><svg viewBox="0 0 10 10"><rect width="10" height="10" rx="2" fill="var(--orange)"/><rect x="2" y="3" width="6" height="4.2" fill="#fff"/><path d="M2 3l3 2.3L8 3" fill="none" stroke="var(--orange)" stroke-width=".7"/></svg>yourdomain@email.com</li>
      <li class="contact"><svg viewBox="0 0 10 10"><rect width="10" height="10" rx="2" fill="var(--orange)"/><circle cx="5" cy="5" r="3" fill="none" stroke="#fff" stroke-width=".7"/><path d="M2 5h6M5 2c-1.5 2-1.5 4 0 6M5 2c1.5 2 1.5 4 0 6" fill="none" stroke="#fff" stroke-width=".6"/></svg>www.yourdomain.com</li>
    </ul>
  </article>

  <!-- Front, orange variant -->
  <article class="card card--light">
    <div class="photo" role="img" aria-label="Photo of a muscular athlete, chest and arms in warm light against a dark background"></div>
    <svg class="shapes" viewBox="0 0 270 607" aria-hidden="true">
      <defs>
        <linearGradient id="band" x1="0" y1="0" x2="0" y2="1">
          <stop offset="0" stop-color="var(--orange-deep)" stop-opacity=".75"/>
          <stop offset=".45" stop-color="var(--orange)"/>
          <stop offset="1" stop-color="var(--orange)"/>
        </linearGradient>
      </defs>
      <polygon points="0,186 64,124 64,170 0,232" fill="var(--orange)"/>
      <polygon points="270,30 270,40 212,98 204,98" fill="var(--grey)"/>
      <polygon points="0,420 180,240 270,170 270,607 0,607" fill="url(#band)"/>
      <polygon points="135,335 270,248 270,260 148,335" fill="var(--white)"/>
      <polygon points="270,520 270,607 178,607" fill="var(--ink)"/>
      <polygon points="228,607 240,607 270,577 270,565" fill="var(--orange)"/>
      <polygon points="150,607 162,607 196,573 184,573" fill="var(--ink)"/>
    </svg>
    <div class="brand"><span class="brand-name">The Kestrel</span><span class="brand-tag">PRIVATE TRAINING STUDIO</span></div>
    <h2 class="kicker">HOW DO YOU</h2>
    <p class="headline-get">GET</p>
    <p class="headline-started">STARTED?</p>
    <svg class="chevrons" viewBox="0 0 36 18" aria-hidden="true"><path d="M2 2l8 7-8 7M12 2l8 7-8 7M22 2l8 7-8 7" fill="none" stroke="var(--white)" stroke-width="3"/></svg>
    <p class="intro">We schedule prospective clients for a no cost or obligation consultation. At that consultation we will do a movement screen with you. This will allow the trainer to see what level of flexibility and strength you are currently at. You will be able to discuss your goals and other issues (injuries, etc) at that time.</p>
  </article>

</main>
</body>
</html>
```